Plumbing Company- Mass mailing Post card

Name of our company is Bramwell plumbing, Inc. Located in West Palm Beach, Florida. Tag line is "Our service is what set's us apart". We're looking for a postcard that we can send as a mass mailing (QPMX). Our clients are high end so we're looking for classy, simple, clean and easy to read (not busy), to represent the kind of work we do, (our work is like no other). Want an attention getter that manages to get the customer to turn the card over for more info.
Include: phone # 561-555-0193, website www.brwplumbing.example, License CFC9073651
Samples that can be included:
-Tap in to 30 plus years of experience.
-Our reputation is our best asset
-Call Bramwell Plumbing today and let us take care of your plumbing needs.
-Bramwell services offered
-We are the difference!
-Serving the Palm Beaches!

Target Market(s)

High end, owners and Property managers

Industry/Entity Type

Plumbing

Font styles to use
Serif

Requirements
Must have
• Tag line
• Classy and clean
Nice to have
• Our original logo color is blue/grey but not opposed if something different is suggested.
• Interested in seeing ideas
Should not have
• Not to be busy looking.

```html
<!DOCTYPE html>
<html lang="en">
<head>
<meta charset="utf-8">
<title>Bramwell Plumbing Postcard</title>
<link href="https://fonts.googleapis.com/css2?family=Montserrat:wght@600;700;800&family=Lato:ital,wght@0,400;0,700;1,400;1,700&display=swap" rel="stylesheet">
<style>
:root{
  --blue:#1f56a8;
  --blue-deep:#123d86;
  --blue-light:#5b8fd6;
  --ink:#2e2e33;
  --grey:#d8dbe0;
  --stage:#eceae6;
  --white:#ffffff;
}
*{margin:0;padding:0;box-sizing:border-box}
html,body{width:900px;height:1200px;overflow:hidden}
body{background:var(--stage);position:relative;font-family:"Lato",Arial,sans-serif;color:var(--ink)}
.card{position:absolute;width:760px;background:var(--white);overflow:hidden;box-shadow:0 4px 14px rgba(0,0,0,.18)}
.front{left:62px;top:68px;height:490px}
.back{left:72px;top:633px;height:492px}
.swoosh{position:absolute;inset:0;width:100%;height:100%}
.brand{position:absolute;display:flex;align-items:center;gap:10px;font-family:"Montserrat",Arial,sans-serif;font-weight:800;color:var(--blue);letter-spacing:.5px;white-space:nowrap;line-height:1}
.brand-dot{border-radius:50%;background:var(--blue)}
.front .brand{left:80px;top:42px;font-size:24px}
.front .brand-dot{width:28px;height:28px}
.back .brand{left:150px;top:14px;font-size:19px}
.back .brand-dot{width:24px;height:24px}
.call{position:absolute;left:440px;top:36px;width:280px;text-align:center;font-weight:700;font-size:12.5px;line-height:1.3}
.phone-pill{position:absolute;left:482px;top:72px;width:196px;height:34px;border-radius:17px;background:var(--blue);border:2px solid var(--blue-light);box-shadow:0 2px 4px rgba(0,0,0,.3);display:flex;align-items:center;justify-content:center;gap:10px;color:var(--white);font-family:"Montserrat",Arial,sans-serif;font-weight:700;font-size:17px}
.headline{position:absolute;left:52px;top:124px;width:700px;font-family:"Montserrat",Arial,sans-serif;font-weight:800;font-size:30.5px;color:var(--ink);white-space:nowrap;letter-spacing:.3px}
.headline span{color:var(--blue)}
.gallery{position:absolute;left:0;top:170px;width:760px;height:164px;background:var(--blue);display:flex;gap:11px;padding:12px 0 0 50px}
.tile{width:125px;height:140px;border:3px solid var(--white);box-shadow:0 1px 3px rgba(0,0,0,.4)}
.t1{background:linear-gradient(135deg,#c9a04a,#6b4a2a)}
.t2{background:linear-gradient(135deg,#e8e3da,#b89b63)}
.t3{background:linear-gradient(135deg,#d8c6a3,#9c8b6e)}
.t4{background:linear-gradient(135deg,#b06a3c,#4a2a1c)}
.t5{background:linear-gradient(135deg,#b9c9c4,#3b4a4a)}
.perks{position:absolute;left:0;top:334px;width:760px;height:122px;background:linear-gradient(90deg,#f3f0ec,#e6e1da)}
.perk{position:absolute;display:flex;align-items:center;gap:10px;font-style:italic;font-weight:700;font-size:14px}
.perk i{width:24px;height:24px;border-radius:50%;background:var(--ink);display:flex;align-items:center;justify-content:center}
.badge{position:absolute;left:590px;top:325px;width:90px;height:90px;border-radius:50%;background:var(--blue);border:4px solid var(--white);box-shadow:0 0 0 2px var(--blue-deep);color:var(--white);text-align:center;font-family:"Montserrat",Arial,sans-serif;font-weight:800;font-size:28px;line-height:1;padding-top:14px}
.badge small{display:block;font-size:10px;font-weight:700}
.ribbon{position:absolute;left:582px;top:384px;width:106px;height:17px;background:var(--blue-deep);color:var(--white);font-size:7px;font-weight:700;text-align:center;line-height:17px;letter-spacing:.3px}
.license{position:absolute;left:585px;top:422px;font-weight:700;font-size:10px}
.footband{position:absolute;left:98px;top:457px;width:662px;height:33px;background:var(--blue);color:var(--white);text-align:center;font-weight:700;font-size:13px;letter-spacing:4px;line-height:33px}
.about{position:absolute;left:16px;top:94px;width:430px}
.section-title{font-family:"Montserrat",Arial,sans-serif;font-weight:700;color:var(--blue-deep);font-size:13px;line-height:16px;letter-spacing:.5px;margin-bottom:5px}
.section-title em{font-style:normal;font-size:11px;color:var(--blue)}
.about p{font-size:9px;line-height:1.25}
.services{position:absolute;left:16px;top:206px;width:440px;font-size:9.5px}
.col{position:absolute;top:22px}
.col.left{left:6px}.col.right{left:196px}
.svc{font-weight:700;line-height:11px;margin-bottom:3px;padding-left:12px;position:relative}
.svc::before{content:"";position:absolute;left:0;top:2px;width:6px;height:8px;border-radius:2px;background:var(--blue)}
.col ul{list-style:none;margin:2px 0 12px 20px;font-style:italic;font-weight:700;font-size:8px;line-height:9.6px}
.col ul li{margin-bottom:3px;padding-left:9px;position:relative}
.col ul li::before{content:"";position:absolute;left:0;top:3px;width:4px;height:4px;border-radius:50%;background:var(--blue-deep)}
.col.left ul{margin-bottom:22px}
.stamp{position:absolute;left:611px;top:26px;width:95px;height:92px;background:#ececee}
.addr{position:absolute;left:484px;width:226px;height:1px;background:#777}
.back-foot{position:absolute;left:38px;top:450px;display:flex;gap:28px;color:var(--white);font-weight:700;font-size:12.5px}
.back-foot span{display:flex;align-items:center;gap:8px}
</style>
</head>
<body>

<section class="card front" aria-label="Postcard front">
  <svg class="swoosh" viewBox="0 0 760 490" preserveAspectRatio="none" aria-hidden="true">
    <path d="M0 0H120C50 50 18 130 30 230C45 340 80 420 100 490H0Z" fill="#3a6fc2"/>
    <path d="M0 0H100C40 55 10 135 20 235C33 340 62 420 80 490H0Z" fill="#111"/>
    <path d="M0 0H84C30 60 4 140 12 240C22 340 46 420 62 490H0Z" fill="#dfe2e6"/>
    <path d="M0 0H66C20 65 -2 145 4 245C12 340 30 420 44 490H0Z" fill="#1f56a8"/>
  </svg>
  <div class="brand"><span class="brand-dot"></span>BRAMWELL PLUMBING</div>
  <p class="call">Call Bramwell Plumbing today and let us take care of your plumbing needs.</p>
  <div class="phone-pill">
    <svg width="18" height="18" viewBox="0 0 24 24" aria-hidden="true"><circle cx="12" cy="12" r="10.5" fill="none" stroke="#fff" stroke-width="2"/><path d="M8.5 7c.6-.5 1.3-.4 1.6.2l.9 1.7c.2.5 0 1-.4 1.3l-.6.4c.6 1.4 1.6 2.5 3 3.1l.4-.6c.3-.4.9-.6 1.3-.4l1.7.9c.6.3.7 1 .2 1.6-1 1-2.5 1.2-3.8.5-2.4-1.3-4.1-3.1-5-5.3-.6-1.3-.3-2.5.7-3.4z" fill="#fff"/></svg>
    561-555-0193
  </div>
  <h1 class="headline">OUR SERVICE IS <span>WHAT SET'S US APART</span></h1>
  <div class="gallery">
    <div class="tile t1" role="img" aria-label="Photo of a gold faucet with crystal handles"></div>
    <div class="tile t2" role="img" aria-label="Photo of a luxury bathroom with freestanding tub filler"></div>
    <div class="tile t3" role="img" aria-label="Photo of a bridge kitchen faucet over a tiled backsplash"></div>
    <div class="tile t4" role="img" aria-label="Photo of a copper kitchen faucet with wheel handle"></div>
    <div class="tile t5" role="img" aria-label="Photo of a chrome tub faucet over a bubbling bath"></div>
  </div>
  <div class="perks" role="img" aria-label="Soft background photo of a bright bathroom"></div>
  <div class="perk" style="left:100px;top:358px"><i><svg width="12" height="12" viewBox="0 0 12 12"><path d="M2 10l8 0M3 6l2 2 4-5" stroke="#fff" stroke-width="1.6" fill="none"/></svg></i>Our reputation is our best asset</div>
  <div class="perk" style="left:100px;top:389px"><i><svg width="12" height="12" viewBox="0 0 12 12"><path d="M2 2l8 8M10 2l-8 8" stroke="#fff" stroke-width="1.8"/></svg></i>Bramwell services offered</div>
  <div class="perk" style="left:340px;top:358px"><i><svg width="12" height="12" viewBox="0 0 12 12"><circle cx="6" cy="6" r="4" fill="none" stroke="#fff" stroke-width="1.5"/></svg></i>We are the difference!</div>
  <div class="perk" style="left:340px;top:389px"><i><svg width="12" height="12" viewBox="0 0 12 12"><path d="M6 11V4M6 4C4 2 2 3 1 4M6 4c2-2 4-1 5 0" stroke="#fff" stroke-width="1.5" fill="none"/></svg></i>Serving the Palm Beaches!</div>
  <div class="badge">30+<small>Years</small></div>
  <div class="ribbon">OF EXPERIENCE</div>
  <p class="license">License CFC9073651</p>
  <div class="footband">www.brwplumbing.example</div>
</section>

<section class="card back" aria-label="Postcard back">
  <svg class="swoosh" viewBox="0 0 760 492" preserveAspectRatio="none" aria-hidden="true">
    <path d="M0 30C120 42 280 56 446 64C280 70 120 74 0 80Z" fill="#1f56a8"/>
    <path d="M0 80C120 74 280 68 446 64C280 74 120 84 0 92Z" fill="#111"/>
    <path d="M472 0H488C472 170 452 330 436 492H422C438 330 458 170 472 0Z" fill="#1f56a8"/>
    <path d="M0 410C110 404 210 406 300 416C210 410 110 412 0 418Z" fill="#111"/>
    <path d="M0 424C150 420 300 428 436 448L431 492H0Z" fill="#1f56a8"/>
  </svg>
  <div class="brand"><span class="brand-dot"></span>BRAMWELL PLUMBING</div>
  <div class="about">
    <h2 class="section-title">ABOUT US</h2>
    <p>Bramwell Plumbing is family owned and operated. With over 30 years in the plumbing industry, we offer highly experienced and skilled plumbers that are licensed and insured. Our master plumbers can provide all facets of plumbing services, from general service and repair work to specialty plumbing needs. We are backflow certified. We also specialize in green technology such as tankless water heaters and water saving toilets.<br>Bramwell Plumbing offers fast, courteous and professional service. We are available 24/7 for your emergency needs, and we are committed to completing your non-emergency service within 48 hours.</p>
  </div>
  <div class="services">
    <h2 class="section-title">OUR SERVICES <em>(COMMERCIAL AND RESIDENTIAL)</em></h2>
    <div class="col left">
      <p class="svc">Plumbing repairs</p>
      <ul><li>Leaky Faucets</li><li>Leaky Water Heaters</li><li>Clogged Drains or Pipes</li></ul>
      <p class="svc">Appliance installation</p>
      <ul><li>Garbage Disposals</li><li>Water Heaters (Tankless, Electric, Gas)</li><li>Gas Grills</li></ul>
    </div>
    <div class="col right">
      <p class="svc">Plumbing maintenance/service</p>
      <ul><li>Drain Cleaning</li><li>Hydro-Jet Drain Cleaning (High Velocity)</li><li>Water Filtration</li><li>Pump, Septic and Grease Trap Cleaning and/or Repair</li></ul>
      <p class="svc">Sewer repair and installation</p>
      <p class="svc">Kitchen and bathroom remodel</p>
      <p class="svc">Appliance installation</p>
      <p class="svc">ADA bathrooms</p>
      <p class="svc">Backflow certifications</p>
      <p class="svc">Drain vision video inspection</p>
      <p class="svc">Complimentary home inspections</p>
    </div>
  </div>
  <div class="stamp"></div>
  <div class="addr" style="top:232px"></div>
  <div class="addr" style="top:276px"></div>
  <div class="addr" style="top:319px"></div>
  <div class="back-foot">
    <span><svg width="15" height="15" viewBox="0 0 24 24" aria-hidden="true"><circle cx="12" cy="12" r="10.5" fill="none" stroke="#fff" stroke-width="2"/><path d="M8.5 7c.6-.5 1.3-.4 1.6.2l.9 1.7c.2.5 0 1-.4 1.3l-.6.4c.6 1.4 1.6 2.5 3 3.1l.4-.6c.3-.4.9-.6 1.3-.4l1.7.9c.6.3.7 1 .2 1.6-1 1-2.5 1.2-3.8.5-2.4-1.3-4.1-3.1-5-5.3-.6-1.3-.3-2.5.7-3.4z" fill="#fff"/></svg>561-555-0193</span>
    <span><svg width="15" height="15" viewBox="0 0 24 24" aria-hidden="true"><circle cx="12" cy="12" r="10" fill="none" stroke="#fff" stroke-width="2"/><path d="M2 12h20M12 2c3 3 3 17 0 20M12 2c-3 3-3 17 0 20" stroke="#fff" stroke-width="1.5" fill="none"/></svg>www.brwplumbing.example</span>
  </div>
</section>

</body>
</html>
```